Shopping center investment profile

We need to design a two-page 8.5" x 11" brochure that can be used as a template for profiling our shopping centers and demonstrating our track record to investors.

Our company (KVM Real Estate Investments) owns retail shopping centers in the southwestern United States. Our website is www.kvmtrh.example, but we will be redesigning and modernizing the website and logo in the near future, so please do not use the color schemes or framework of the website for the brochure.

Our investors are institutional and high net worth investors who typically have an existing relationship with our company. They are determining whether to invest multi-millions of dollars in a shopping center opportunity, so the brochure needs to be professional, very high quality and provide key information about the specific property.
Updates

Additional guidance on color scheme:

We would like to see a Blue (something like Hex #5A61BC) and Gold (Hex #EDB215) or (Hex #DDA24B) color scheme with some Black accents 

Thank you!

Target Market(s)

Our target audiences are institutional investors, high net-worth individuals, financial firms and medium to large commercial real estate companies.

Industry/Entity Type

Investment

Requirements
Must have
• Clean and modern look with corresponding fonts and colors.
• Incorporates the information found in the attached "Marlowe Crossing profile" Pages or PDF file.
• Final file design files that can be modified easily
Nice to have
• Two examples of industry brochures are attached. These are examples of the professional quality that we are looking for, not necessarily the design or format.

```html
<!DOCTYPE html>
<html lang="en">
<head>
<meta charset="utf-8">
<title>Marlowe Crossing – Property Profile</title>
<link rel="stylesheet" href="https://fonts.googleapis.com/css2?family=Michroma&family=Exo+2:wght@400;600;700&display=swap">
<style>
:root{
  --blue:#5a61bc;
  --blue-dark:#3c3f8e;
  --navy:#2c2e6e;
  --lavender:#8d92d4;
  --gold:#edb215;
  --gold-soft:#dda24b;
  --cream:#f8ebbd;
  --ink:#1b1c45;
  --white:#ffffff;
}
*{box-sizing:border-box;margin:0;padding:0}
html,body{width:852px;height:1200px;overflow:hidden;background:#fff}
body{position:relative;font-family:"Exo 2",sans-serif;color:var(--ink)}
.page{position:absolute;left:98px;width:698px;height:565px;overflow:hidden}
.page-front{top:25px;background:var(--blue)}
.page-back{top:615px;background:var(--navy)}
.abs{position:absolute}

/* front: spine */
.spine{left:0;top:0;width:144px;height:565px;background:var(--blue)}
.spine-tab{left:36px;top:0;width:34px;height:41px;background:var(--gold)}
.spine-title{left:36px;top:466px;width:380px;transform-origin:0 0;transform:rotate(-90deg);white-space:nowrap;color:var(--gold)}
.spine-title .name{font-family:"Michroma",sans-serif;font-size:20px;letter-spacing:4px;line-height:1.2}
.spine-title .sub{font-family:"Michroma",sans-serif;font-size:9px;letter-spacing:3px;text-align:right;margin-top:4px}
.spine-address{left:8px;top:490px;width:136px;color:var(--gold);font-weight:700;font-size:9.5px;line-height:1.3;text-transform:uppercase;text-align:center}
.spine-rule{left:144px;top:0;width:11px;height:565px;background:var(--navy)}

/* front: cream column */
.story{left:155px;top:0;width:259px;height:565px;background:var(--cream)}
.photo{background:linear-gradient(180deg,#8fb4d8 0%,#b6c9b0 45%,#a4704e 65%,#8b8a86 100%)}
.story .photo{left:12px;top:10px;width:234px;height:123px}
.section-bar{height:15px;background:var(--gold);color:var(--white);font-weight:700;font-size:10px;letter-spacing:.5px;padding:1px 8px;text-transform:uppercase}
.story .opportunity-bar{left:8px;top:176px;width:244px}
.story .results-bar{left:8px;top:393px;width:244px}
.bullets{list-style:none;width:236px;font-size:9px;font-weight:600;color:var(--blue-dark);line-height:1.2}
.bullets li{position:relative;padding:3px 0 3px 10px;border-bottom:1px solid #d8c98a}
.bullets li::before{content:"";position:absolute;left:1px;top:7px;width:5px;height:5px;border-radius:50%;background:var(--blue-dark)}
.story .opportunity-list{left:14px;top:194px}
.story .results-list{left:14px;top:410px}

/* front: data panel */
.data-panel{left:414px;top:0;width:284px;height:565px;background:var(--blue)}
.table-card{left:25px;width:248px}
.table-head{height:16px;background:var(--navy);color:var(--white);font-weight:700;font-size:10px;letter-spacing:.6px;padding:2px 10px;text-transform:uppercase}
.table-body{padding:8px 10px}
.summary{top:27px}
.summary .table-body{background:var(--lavender);height:180px;padding-top:22px}
.investment{top:221px}
.investment .table-body{background:var(--blue-dark);height:193px;padding-top:26px}
.row{display:flex;justify-content:space-between;font-size:8.5px;font-weight:700;padding:3px 0;border-bottom:1px solid rgba(255,255,255,.25)}
.summary .row{color:var(--navy)}
.investment .row{color:var(--white)}
.structure-list{list-style:none;text-align:right;font-size:8px;line-height:1.3}
.structure-list li::before{content:"● ";}
.contact{left:60px;top:473px;width:164px;text-align:center;color:var(--white);font-size:7px;line-height:1.35}
.contact strong{font-weight:600;display:block;margin-bottom:2px}
.contact-block{top:481px;width:48px;height:34px;background:#b9bce4}
.contact-block.left{left:8px}
.contact-block.right{left:230px}

/* back */
.gallery{left:0;top:0;width:272px;height:565px;background:var(--navy)}
.gallery .label{left:4px;color:var(--gold);font-weight:700;font-size:9px;text-transform:uppercase}
.label-before{top:33px}
.label-after{top:209px}
.gallery .photo{left:4px;width:260px;height:147px}
.photo-before{top:49px}
.photo-after{top:226px}
.site-plan{left:4px;top:381px;width:260px;height:165px;background:linear-gradient(160deg,#c8dfb2,#a9b7c9 60%,#e8e2cf)}
.gold-stripe{left:272px;top:0;width:14px;height:565px;background:var(--gold)}
.back-main{left:286px;top:0;width:412px;height:565px;background:var(--blue-dark)}
.back-title{left:18px;top:30px;width:360px;color:var(--gold);text-align:right}
.back-title .name{font-family:"Michroma",sans-serif;font-size:17px;letter-spacing:4px;text-align:left;white-space:nowrap}
.back-title .sub{font-family:"Michroma",sans-serif;font-size:9px;letter-spacing:3px;margin-top:6px}
.challenges-head{left:22px;top:127px;color:var(--gold);font-weight:700;font-size:11px;letter-spacing:.4px;text-transform:uppercase}
.challenges{left:22px;top:172px;width:376px;column-count:2;column-gap:14px;color:var(--white);font-size:8.8px;line-height:1.35}
.challenges p{margin-bottom:10px;padding-left:8px;position:relative}
.challenges p::before{content:"";position:absolute;left:0;top:4px;width:5px;height:5px;border-radius:50%;background:var(--gold)}
.challenges b{color:var(--gold);font-weight:700;text-transform:uppercase}
.tenants{left:28px;top:385px;width:300px;display:flex;gap:12px;align-items:center}
.tenant{background:var(--white);height:62px;display:flex;align-items:center;justify-content:center;font-weight:700;font-size:11px;color:var(--navy);padding:0 10px}
.tenant.wide{width:104px}
.tenant.short{height:26px;width:96px}
.back-footer{left:18px;top:505px;width:380px;border-top:1px solid var(--gold);padding-top:8px;text-align:center;color:var(--gold);font-weight:700;font-size:8px}
</style>
</head>
<body>

<section class="page page-front">
  <div class="abs spine"></div>
  <div class="abs spine-tab"></div>
  <div class="abs spine-title">
    <div class="name">MARLOWE CROSSING</div>
    <div class="sub">Property Profile</div>
  </div>
  <div class="abs spine-address">SWC of Marlowe Rd<br>and Fairline Rd<br>Cedar Vale, Arizona</div>
  <div class="abs spine-rule"></div>

  <div class="abs story">
    <div class="abs photo" role="img" aria-label="Photo of the renovated shopping center storefronts"></div>
    <div class="abs section-bar opportunity-bar">Opportunity</div>
    <ul class="abs bullets opportunity-list">
      <li>Bank owned property with attractive purchase price</li>
      <li>Strong relationship with seller's broker and decision makers</li>
      <li>Redevelopment upside with management and leasing</li>
      <li>No major renovations required</li>
      <li>Cedar Vale location has very strong population, education and income demographics</li>
      <li>Adjacent to premier 2,500-residence master planned community of Cobalt Ridge Lakes</li>
      <li>Strong employment area with the new Northgate Medical hospital and the adjacent Halvern Cancer center</li>
    </ul>
    <div class="abs section-bar results-bar">Results</div>
    <ul class="abs bullets results-list">
      <li>Stabilized the shopping center within three years, producing excellent results for investors</li>
      <li>Transformed the center into a vibrant destination that the surrounding community is excited about</li>
      <li>Transitioned legacy tenants to upgrade the business operators</li>
      <li>Reduced the shopping center's operating expenses by replacing vendors and appealing property taxes</li>
    </ul>
  </div>

  <div class="abs data-panel">
    <div class="abs table-card summary">
      <div class="table-head">Summary</div>
      <div class="table-body">
        <div class="row"><span>Property Type</span><span>Shopping Center</span></div>
        <div class="row"><span>Size</span><span>70,400 sq ft</span></div>
        <div class="row"><span>Purchased</span><span>April 2011</span></div>
        <div class="row"><span>Total Investment</span><span>$X,XXX,XXX</span></div>
        <div class="row"><span>Purchase Occupancy</span><span>8.30%</span></div>
        <div class="row"><span>Current Occupancy</span><span>97.20%</span></div>
        <div class="row"><span>Projected 5-year IRR (Unleveraged)</span><span>XX.XX%</span></div>
      </div>
    </div>
    <div class="abs table-card investment">
      <div class="table-head">Investment Information</div>
      <div class="table-body">
        <div class="row"><span>Purchase Price</span><span>$X,XXX,XXX</span></div>
        <div class="row"><span>Sponsor Acquisition Fee</span><span>$XX,XXX</span></div>
        <div class="row"><span>Painting and Landscape</span><span>$XXX,XXX</span></div>
        <div class="row"><span>TI/LC Reserve</span><span>$X,XXX,XXX</span></div>
        <div class="row"><span>Operating Expenses</span><span>$XXX,XXX</span></div>
        <div class="row"><span>Total Cash Investment</span><span></span></div>
        <div class="row"><span>Investor / Sponsor Split</span><span>XX% / XX%</span></div>
        <div class="row" style="border:0"><span>Structure</span>
          <ul class="structure-list"><li>Cash Flow Pari Passu</li><li>Acquisition Fee</li><li>Management Fee</li></ul>
        </div>
      </div>
    </div>
    <div class="abs contact-block left"></div>
    <div class="abs contact">
      <strong>KVM Real Estate Investments</strong>
      410 S Harrow Way Suite 200<br>Mesa, AZ 85200<br>Ph. (555) 014-2290
    </div>
    <div class="abs contact-block right"></div>
  </div>
</section>

<section class="page page-back">
  <div class="abs gallery">
    <div class="abs label label-before">Before – 8% occupancy</div>
    <div class="abs photo photo-before" role="img" aria-label="Photo of the shopping center before renovation"></div>
    <div class="abs label label-after">After – 97% occupancy</div>
    <div class="abs photo photo-after" role="img" aria-label="Rendering of the shopping center after renovation"></div>
    <div class="abs site-plan" role="img" aria-label="Site plan of the shopping center and parking"></div>
  </div>
  <div class="abs gold-stripe"></div>

  <div class="abs back-main">
    <div class="abs back-title">
      <div class="name">MARLOWE CROSSING</div>
      <div class="sub">Property Profile</div>
    </div>
    <div class="abs challenges-head">Challenges &amp; Solutions</div>
    <div class="abs challenges">
      <p><b>Nationwide vacancy rate</b> – KVM did significant due diligence on the property before purchasing the asset, and determined that the location is an A/A+. Tenant improvement and leasing commissions were reserved in order to attract national and regional tenants</p>
      <p><b>Size of anchor space</b> – KVM determined that a family-friendly entertainment venue would best serve the demographics in the area instead of another grocer. KVM sought out an experienced operator in Tall Tails, who has multiple locations in three states</p>
      <p><b>Curb appeal</b> – With vacancy and a stigma attached to the center, KVM had to change the center's appeal to the community. KVM worked hand in hand with the Town of Cedar Vale and the Cobalt Ridge Lakes community association to paint the center, upgrade landscaping and add new and larger monument signs</p>
    </div>
    <div class="abs tenants">
      <div class="tenant" style="width:70px">Party Place</div>
      <div class="tenant wide">Tall Tails</div>
      <div class="tenant short">Bluefern</div>
    </div>
    <div class="abs back-footer">KVM Real Estate Investments: 410 S Harrow Way Suite 200 Mesa, AZ 85200 Ph. (555) 014-2290</div>
  </div>
</section>

</body>
</html>
```